Off Campus Housing website service for universities needs corporate brochure

We need a corporate brochure targeted at universities to get them to partner with us to offer an Off-Campus Housing website with housing listings and educational resources for their students. We provide hosted software and support, off-campus housing listings, and educational resources to embed in the university website (i.e http://rentalhub.brx.edu); the university promotes the service to off-campus students, parents, and faculty/staff. We have a dedicated account executive to work with each university to promote the website to property managers in the schools area who pay to list their properties on the site. We currently partner with over 100 colleges and universities across the country to serve the needs of their off-campus students. Our corporate website is: www.lodgebridgealliance.com.
Updates

Target Market(s)

Universities and Colleges

Industry/Entity Type

Marketing

Font styles to use
Serif

Requirements
Must have
• Our logo
• Our website (www.lodgebridgealliance.com)
• Contact information (this is different than what we used on our previous brochure, image attached):
• Email: sales@lodgebridgealliance.com
• Student image(s) - must be diverse
• Phone: 866-402-7719
Nice to have
• University/Campus image (generic)

```html
<!DOCTYPE html>
<html lang="en">
<head>
<meta charset="utf-8">
<title>Lodgebridge Alliance – Trifold Brochure</title>
<link rel="stylesheet" href="https://fonts.googleapis.com/css2?family=Playfair+Display:wght@700;900&family=Open+Sans:wght@400;600;700;800&display=swap">
<style>
  :root {
    --blue-deep: #173f86;
    --blue: #1f57b0;
    --blue-light: #3a78d1;
    --orange: #f2a11f;
    --white: #ffffff;
    --ink: #3a3f4a;
    --page-bg: #e8eaee;
  }
  * { box-sizing: border-box; margin: 0; padding: 0; }
  html, body { width: 900px; height: 1200px; overflow: hidden; }
  body {
    background: var(--page-bg);
    font-family: "Open Sans", Arial, sans-serif;
    color: var(--ink);
    position: relative;
  }
  .brochure {
    position: absolute;
    left: 10px; top: 260px;
    width: 880px; height: 680px;
    display: grid;
    grid-template-columns: repeat(3, 1fr);
    background: var(--white);
  }
  .panel { position: relative; height: 680px; overflow: hidden; }
  .serif { font-family: "Playfair Display", Georgia, serif; }

  /* footer strip */
  .panel-footer {
    position: absolute; left: 0; right: 0; bottom: 0; height: 34px;
    background: var(--blue-deep);
    color: var(--white);
    font-size: 11px; font-weight: 600; letter-spacing: .3px;
    display: flex; align-items: center; justify-content: center;
  }
  .panel-footer.accent { border-top: 6px solid var(--orange); height: 40px; }

  /* left panel */
  .campus-photo {
    height: 230px;
    background: linear-gradient(180deg, #8fb6e0 0%, #cfdce9 45%, #e9e3d6 62%, #6b8c4a 80%, #4f6e36 100%);
  }
  .section-bar {
    height: 46px; background: var(--blue);
    border-left: 10px solid var(--orange);
    display: flex; align-items: center; padding-left: 18px;
    color: var(--white); font-size: 24px; letter-spacing: 1px;
  }
  .left-body { padding: 16px 20px 0; font-size: 9.5px; line-height: 1.55; }
  .left-body p { margin-bottom: 10px; }
  .offer-heading {
    color: var(--blue); font-weight: 800; font-size: 11px; letter-spacing: .6px;
    margin: 4px 0 8px;
  }
  .offer-list { list-style: none; }
  .offer-list li { display: flex; gap: 8px; align-items: flex-start; margin-bottom: 8px; }
  .offer-list svg { flex: 0 0 12px; margin-top: 2px; }

  /* middle panel */
  .panel-middle {
    background: linear-gradient(180deg, var(--blue-light) 0%, var(--blue) 55%, var(--blue-deep) 100%);
    color: var(--white);
  }
  .building-backdrop {
    position: absolute; left: 0; right: 0; top: 280px; height: 230px;
    background: linear-gradient(180deg, rgba(255,255,255,0) 0%, rgba(255,255,255,.14) 50%, rgba(255,255,255,0) 100%);
  }
  .history-tab {
    position: absolute; right: 0; top: 20px;
    width: 140px; height: 36px; background: var(--orange);
    color: var(--white); font-size: 18px; letter-spacing: 1px;
    display: flex; align-items: center; padding-left: 16px;
  }
  .middle-body {
    position: absolute; top: 76px; left: 22px; right: 22px;
    font-size: 9.5px; line-height: 1.6;
  }
  .middle-body p { margin-bottom: 12px; }
  .join-heading {
    position: absolute; left: 0; right: 0; top: 520px;
    text-align: center; font-size: 20px; color: var(--white); letter-spacing: .5px;
  }
  .contact-lines {
    position: absolute; left: 0; right: 0; top: 566px;
    text-align: center; font-size: 10px; line-height: 1.7; font-weight: 600;
  }

  /* right panel */
  .logo-band {
    height: 70px; background: var(--blue-deep);
    display: flex; align-items: center; justify-content: center;
  }
  .logo-name {
    font-family: "Playfair Display", Georgia, serif; font-weight: 700;
    color: var(--white); font-size: 21px; letter-spacing: 1.5px;
  }
  .students-photo {
    height: 280px;
    background: linear-gradient(180deg, #e9edf2 0%, #d6c2ad 45%, #7c8fae 75%, #4a5f85 100%);
  }
  .tagline-band {
    background: var(--blue); color: var(--white);
    text-align: center; padding: 14px 14px 12px;
  }
  .tagline-band h2 { font-size: 15px; font-weight: 800; letter-spacing: .4px; }
  .tagline-band p { font-size: 10px; margin-top: 5px; line-height: 1.4; }
  .since {
    text-align: center; color: var(--orange);
    font-size: 36px; margin-top: 20px; letter-spacing: 1px;
  }
  .since-text {
    text-align: center; font-size: 10px; line-height: 1.55;
    padding: 8px 28px 0;
  }
</style>
</head>
<body>
  <main class="brochure">

    <section class="panel panel-left">
      <div class="campus-photo" role="img" aria-label="Photo of a classic university building with white columns on a green lawn"></div>
      <h2 class="section-bar serif">VISION</h2>
      <div class="left-body">
        <p>Lodgebridge Alliance works with colleges and universities to deliver a complete off-campus housing program. We host the software, supply the listings and provide educational resources that embed right in the university website, such as http://rentalhub.brx.edu.</p>
        <p>Our goal is simple: help every student find safe, affordable housing near campus while giving the university a trusted, branded resource it can promote with pride.</p>
        <h3 class="offer-heading">WE OFFER</h3>
        <ul class="offer-list">
          <li><svg width="12" height="12" viewBox="0 0 12 12"><path d="M1.5 6.5l3 3 6-7" fill="none" stroke="#1f57b0" stroke-width="2"/></svg>Hosted software and full technical support for your housing website</li>
          <li><svg width="12" height="12" viewBox="0 0 12 12"><path d="M1.5 6.5l3 3 6-7" fill="none" stroke="#1f57b0" stroke-width="2"/></svg>A dedicated account executive for your campus area</li>
          <li><svg width="12" height="12" viewBox="0 0 12 12"><path d="M1.5 6.5l3 3 6-7" fill="none" stroke="#1f57b0" stroke-width="2"/></svg>Verified local listings from area property managers</li>
          <li><svg width="12" height="12" viewBox="0 0 12 12"><path d="M1.5 6.5l3 3 6-7" fill="none" stroke="#1f57b0" stroke-width="2"/></svg>Educational guides for students, parents and staff</li>
        </ul>
      </div>
      <footer class="panel-footer">www.lodgebridgealliance.com</footer>
    </section>

    <section class="panel panel-middle">
      <div class="building-backdrop" role="img" aria-label="Faint backdrop of a campus building"></div>
      <h2 class="history-tab serif">HISTORY</h2>
      <div class="middle-body">
        <p>Since 2000 we have partnered with over 100 colleges and universities across the country to serve the needs of their off-campus students.</p>
        <p>Property managers in your area pay to list their rentals, so the program is offered at no cost to the university or its students.</p>
        <p>Your school promotes the service to students, parents and faculty, and we take care of the rest from setup to daily support.</p>
      </div>
      <h2 class="join-heading serif">JOIN YOUR COLLEAGUES!</h2>
      <div class="contact-lines">
        <div>sales@lodgebridgealliance.com</div>
        <div>866-402-7719</div>
      </div>
      <footer class="panel-footer accent">www.lodgebridgealliance.com</footer>
    </section>

    <section class="panel panel-right">
      <div class="logo-band"><span class="logo-name">LODGEBRIDGE ALLIANCE</span></div>
      <div class="students-photo" role="img" aria-label="Photo of a diverse group of smiling university students holding books"></div>
      <div class="tagline-band">
        <h2>MORE THAN JUST A WEBSITE</h2>
        <p>a custom designed off-campus housing program for your unique campus</p>
      </div>
      <h2 class="since serif">SINCE 2000</h2>
      <p class="since-text">Our company has been working with universities to create a trusted source for off-campus housing.</p>
      <footer class="panel-footer">www.lodgebridgealliance.com</footer>
    </section>

  </main>
</body>
</html>
```